Stationery Refresh For Local Mortgage Broker

We want to modernise and standardise our stationery, including: letterhead, presentation folder, email signature and business card.

The new stationery should be a more modern and professional take on our existing colour scheme and brand. (We do not want a complete overhaul.) A folder of approved stock photos can be found here: https://filebox.example-share.net/f/7kQzR2mTn4vWx9Lp3Yb8-HsdJe5Uc1Ga/view

Our current website is: www.brindlecovefin.com.au but we will be updating this to be consistent with our new stationery.

We are open to *very slight* tweaks to our logo if you feel it needs modernising, but overall we would like to maintain consistent colour scheme.

> Letterhead

148 Calloway Parade,
Geelong, VIC, 3220
ABN: 31 805 249 067
Australian Credit License: 718293

(03) 5391 6084
www.brindlecovefin.com.au

> Presentation Folder

148 Calloway Parade,
Geelong, VIC, 3220
(03) 5391 6084
www.brindlecovefin.com.au

ABN: 31 805 249 067

> Email Signature

Liam Tresidder
Director
M. 0412 857 294
P. (03) 5391 6084
www.brindlecovefin.com.au
148 Calloway Parade,
Geelong, VIC, 3220

ABN: 31 805 249 067

(you can also include a photo if you like: https://brindlecovefin.com.au/wp-content/uploads/2020/12/Liam-Tresidder.png.webp)

> Business Card

Liam Tresidder
Director
M. 0412 857 294
P. (03) 5391 6084
www.brindlecovefin.com.au
148 Calloway Parade,
Geelong, VIC, 3220

ABN: 31 805 249 067

Additional information...

If it's useful/relevant, the services we offer are: Home Loans, Investment Loans, Refinance, Debt Consolidation, Commercial Finance, Vehicle Loans
(You may choose to use this in any of the designs)

Target Market(s)

Home Buyers and Investors

Industry/Entity Type

Mortgage broking/property/real estate

Requirements
Must have
• At least somewhat consistent with our current site (yet meaningfully modernized)
Should not have
• dramatically different logo or colourscheme overhauls

```html
<!DOCTYPE html>
<html lang="en">
<head>
<meta charset="utf-8">
<title>Brindlecove Finance – Business Card</title>
<link rel="stylesheet" href="https://fonts.googleapis.com/css2?family=Roboto:wght@400;500;700&display=swap">
<style>
  :root {
    --bg: #d2d6d7;
    --card: #f3f2ef;
    --brand-red: #8e0f12;
    --ink: #2b2b2b;
    --rule: #3a3a3a;
  }
  * { box-sizing: border-box; margin: 0; padding: 0; }
  html, body { width: 1200px; height: 1049px; overflow: hidden; }
  body {
    background: var(--bg);
    font-family: "Roboto", Arial, sans-serif;
    color: var(--ink);
    display: flex;
    flex-direction: column;
    align-items: center;
    justify-content: center;
    gap: 48px;
  }
  .card {
    width: 640px;
    height: 366px;
    background: var(--card);
    border-bottom: 5px solid var(--brand-red);
    position: relative;
    box-shadow: 0 10px 24px rgba(0,0,0,0.12);
  }
  .brand {
    display: flex;
    align-items: center;
    gap: 10px;
    color: var(--brand-red);
    font-weight: 500;
    text-transform: uppercase;
    letter-spacing: 0.18em;
    white-space: nowrap;
  }
  .brand-mark { width: 10px; height: 10px; background: var(--brand-red); flex: none; }

  /* Front */
  .card-front .brand {
    position: absolute;
    left: 36px;
    top: 140px;
    width: 260px;
    font-size: 14px;
  }
  .divider { position: absolute; left: 320px; width: 1px; background: var(--rule); }
  .divider-top { top: 92px; height: 36px; }
  .divider-main { top: 140px; height: 130px; }
  .contact { position: absolute; left: 338px; top: 92px; font-size: 15px; line-height: 1.3; }
  .contact-name { color: var(--brand-red); font-weight: 700; font-size: 16px; letter-spacing: 0.02em; }
  .contact-role { margin-bottom: 12px; }
  .contact-address { margin-bottom: 8px; }
  .contact-line { display: flex; align-items: center; gap: 8px; }
  .contact-line svg { width: 14px; height: 14px; flex: none; fill: var(--brand-red); }
  .legal { position: absolute; left: 36px; right: 36px; bottom: 30px; font-size: 15px; }
  .legal-sep { color: var(--brand-red); font-weight: 700; margin: 0 6px; }

  /* Back */
  .card-back { display: flex; flex-direction: column; align-items: center; justify-content: center; gap: 36px; }
  .card-back .brand { font-size: 26px; letter-spacing: 0.22em; }
  .services { font-size: 13px; text-align: center; line-height: 1.7; max-width: 520px; }
  .services .dot { display: inline-block; width: 6px; height: 6px; border-radius: 50%; background: var(--brand-red); margin: 0 6px; vertical-align: middle; }
</style>
</head>
<body>

<section class="card card-front">
  <div class="brand"><span class="brand-mark"></span>Brindlecove Finance</div>

  <span class="divider divider-top"></span>
  <span class="divider divider-main"></span>

  <div class="contact">
    <p class="contact-name">LIAM TRESIDDER</p>
    <p class="contact-role">Director</p>
    <p class="contact-address">148 Calloway Parade,<br>Geelong, VIC, 3220</p>
    <p class="contact-line">
      <svg viewBox="0 0 16 16" aria-hidden="true"><path d="M4 1h8a1 1 0 0 1 1 1v12a1 1 0 0 1-1 1H4a1 1 0 0 1-1-1V2a1 1 0 0 1 1-1zm1 2v9h6V3H5zm3 10.2a.7.7 0 1 0 0-.01z"/></svg>
      0412 857 294
    </p>
    <p class="contact-line">
      <svg viewBox="0 0 16 16" aria-hidden="true"><path d="M1 6c0-2 3-3 7-3s7 1 7 3v1h-3V5.5C11 5 9.5 5 8 5s-3 0-4 .5V7H1zm3 2h8l2 6H2zm4 1.5a2 2 0 1 0 0 4 2 2 0 0 0 0-4z"/></svg>
      (03) 5391 6084
    </p>
    <p class="contact-line">
      <svg viewBox="0 0 16 16" aria-hidden="true"><path d="M1 3h14v10H1zm1.5 1.2L8 8.5l5.5-4.3z"/></svg>
      info@brindlecovefin.com.au
    </p>
    <p class="contact-line">
      <svg viewBox="0 0 16 16" aria-hidden="true"><circle cx="8" cy="8" r="7"/></svg>
      www.brindlecovefin.com.au
    </p>
  </div>

  <p class="legal">ABN: 31 805 249 067<span class="legal-sep">|</span>Australian Credit License: 718293</p>
</section>

<section class="card card-back">
  <div class="brand"><span class="brand-mark"></span>Brindlecove Finance</div>
  <p class="services">
    Home Loans<span class="dot"></span>Investment Loans<span class="dot"></span>Refinance<span class="dot"></span>Debt Consolidation<br>
    Commercial Finance<span class="dot"></span>Vehicle Loans
  </p>
</section>

</body>
</html>
```